Business Identity Stationary

Already have the logo which is in the attached files so only need the Business STationary
1) Double Sided Business Card
2) Letterhead
3) Presentation folder with business card holder on inside cover
4) WIth compliments slip
See information for business cards, letterhead and presentation folder below.
http://files.pixelbazaar-example.com/img/771204/40612/40612_3918825_771204_thumb.jpg
Updates

This should be a simply job using a logo we already had designed along with a little device. I suggest using the device off center and perhaps lower in the corner in an abstract way. Also the logo device could be used as a watermark for the letterhead. The designer who created the logo presented something that I think works well for a business card. The front of the double sided business card could have the name logo small for the website address and only use the Lime device on the front. Then on the back could be the name Brevar Consulting logo.

Please note that for the business card the black and lime green background do look good. Also please think of using the lime device separately in an unusual way.

It has been brought to my attention that.my budget was far to low. Hopefully this.will attract you to the project. 

The parent company of Brevar Consulting is TallHeron investments. I have uploaded a file of the Tall Heron business card I really like. Perhaps use this business card as a guide to the type of modern and clean style I am looking for. It also works to have the Brevar Consultign and Tall Heron similar.

Reason: Still haven't received anything exactly right.

Industry/Entity Type

Business

Font styles to use
Sans Serif

Colors
9bcb3c
000000
5c5c5c
add136
cadf82
eaf2cf
f9fbf2
1b1b1b
757575

Requirements
Must have
• 1) Double Sided Business Card
Marta Delvorin
Director
Tel: +505 8290 3357
Email: mkd@brevarconsulting-example.com
Website: www.brevarconsulting-example.com

Everett Delvorin
Director
Tel: +505 8290 3362
Email: ekd@brevarconsulting-example.com

Lucia Pardo Ventrosa
Director
Tel: 8442 6183
Email: lpv@brevarconsulting-example.com

2) Letterhead
Logo
Lime Logo Device
Website Address: www.brevarconsulting-example.com
Small print on bottom: Brevar Consulting a Tall Heron Investment Company SA. RUC K0720000483915

3) Presentation Folder
Traditional Presentation folder with inside front cover spot for the insertion of business card.

4) With Compliments slip

```html
<!DOCTYPE html>
<html lang="en">
<head>
<meta charset="utf-8">
<title>Brevar Consulting – Business Cards</title>
<link rel="stylesheet" href="https://fonts.googleapis.com/css2?family=Ubuntu:wght@400;500&display=swap">
<style>
  :root {
    --lime: #add136;
    --lime-deep: #9bcb3c;
    --black: #000000;
    --ink: #1b1b1b;
    --grey: #5c5c5c;
    --grey-light: #757575;
    --white: #ffffff;
    --backdrop: #2a2a2a;
  }
  * { box-sizing: border-box; margin: 0; padding: 0; }
  html, body {
    width: 1200px; height: 960px; overflow: hidden;
    background: var(--backdrop);
    font-family: "Ubuntu", sans-serif;
  }
  .canvas { position: relative; width: 1200px; height: 960px; }

  .card {
    position: absolute; width: 700px; height: 400px; overflow: hidden;
    background: radial-gradient(ellipse at 55% 40%, #262626 0%, var(--ink) 45%, #0b0b0b 100%);
  }
  .card--contact { left: 440px; top: 40px; }
  .card--brand { left: 60px; top: 500px; }

  /* contact side */
  .person { position: absolute; left: 50px; top: 44px; color: var(--lime); text-transform: uppercase; }
  .person__name { font-size: 30px; font-weight: 400; letter-spacing: 1.5px; }
  .person__role { font-size: 17px; letter-spacing: 1px; margin-top: 2px; }
  .contact-list { position: absolute; left: 50px; top: 138px; list-style: none; color: var(--lime); text-transform: uppercase; font-size: 19px; letter-spacing: 0.8px; }
  .contact-list li { display: flex; align-items: center; gap: 14px; height: 40px; }
  .contact-list svg { width: 24px; height: 24px; fill: var(--lime); flex: none; }

  .web-band {
    position: absolute; left: 0; top: 236px; width: 560px; height: 58px;
    background: var(--lime); display: flex; align-items: center;
  }
  .web-band__url { padding-left: 56px; font-size: 19px; letter-spacing: 1px; text-transform: uppercase; color: var(--black); flex: 1; }
  .stripes { display: flex; height: 100%; }
  .stripes span { width: 26px; border-left: 2px solid var(--black); height: 100%; }

  .signature { position: absolute; right: 40px; bottom: 36px; display: flex; align-items: center; gap: 10px; color: var(--grey-light); font-size: 15px; letter-spacing: 0.5px; }
  .dot { width: 18px; height: 18px; border-radius: 50%; background: var(--lime-deep); }

  /* brand side */
  .brand-name { position: absolute; left: 70px; top: 150px; display: flex; align-items: center; gap: 16px; color: var(--white); font-size: 46px; font-weight: 500; letter-spacing: 2px; text-transform: uppercase; }
  .brand-name .dot { width: 26px; height: 26px; }
  .brand-band {
    position: absolute; left: 470px; top: 218px; width: 230px; height: 96px;
    background: var(--lime); display: flex;
  }
  .brand-band .stripes span { width: 28px; }
</style>
</head>
<body>
<main class="canvas">

  <section class="card card--contact" aria-label="Business card, contact side">
    <div class="person">
      <h1 class="person__name">Marta Delvorin</h1>
      <p class="person__role">Director</p>
    </div>
    <ul class="contact-list">
      <li>
        <svg viewBox="0 0 24 24" aria-hidden="true"><path d="M6.6 10.8c1.4 2.8 3.8 5.1 6.6 6.6l2.2-2.2c.3-.3.7-.4 1-.2 1.1.4 2.3.6 3.6.6.6 0 1 .4 1 1V20c0 .6-.4 1-1 1C10.6 21 3 13.4 3 4c0-.6.4-1 1-1h3.5c.6 0 1 .4 1 1 0 1.3.2 2.5.6 3.6.1.3 0 .7-.2 1z"/></svg>
        <span>+505 8290 3357</span>
      </li>
      <li>
        <svg viewBox="0 0 24 24" aria-hidden="true"><path d="M2 5h20v14H2z M3.5 6.5v.4L12 13l8.5-6.1v-.4z" fill-rule="evenodd"/></svg>
        <span>mkd@brevarconsulting-example.com</span>
      </li>
    </ul>
    <div class="web-band">
      <span class="web-band__url">www.brevarconsulting-example.com</span>
      <div class="stripes"><span></span><span></span><span></span></div>
    </div>
    <div class="signature"><span class="dot"></span><span>Brevar Consulting</span></div>
  </section>

  <section class="card card--brand" aria-label="Business card, brand side">
    <div class="brand-name"><span>Brevar Consulting</span><span class="dot"></span></div>
    <div class="brand-band">
      <div class="stripes"><span></span><span></span><span></span><span></span></div>
    </div>
  </section>

</main>
</body>
</html>
```